Book Cover Design Project

I need a book cover for my new upcoming book called "Silent Tee Stance".
The book is mental golf book and all about how the subconscious mind drives your decisions, emotions and actions.
I want a head or skull or brain design with a fairway placed inside the logo.
Also thinking a design of a landscape of a golf hole in the mind logo.. Just throwing our ideas to your designers
Thanks

Reason: I want to invite other designers

Reason: I would like to invite more designers to the project

Reason: Not getting designs I am looking for .

Reason: Designs not ready

Reason: need further design work on current designs

Reason: finalizing drafts :)

Reason: working with one designer to finalize book cover

Target Market(s)

golfers who want to find their true peak performance and people who want to improve their own lives and personal performance

Industry/Entity Type

Landscape

Requirements
Must have
• golf in mind
brain design
fairway design
Nice to have
• golf on cover

```html
<!DOCTYPE html>
<html lang="en">
<head>
<meta charset="utf-8">
<title>GOLF Silent Tee Stance – Book Cover</title>
<link rel="stylesheet" href="https://fonts.googleapis.com/css2?family=Tinos:wght@400;700&family=Arimo:wght@400&display=swap">
<style>
  :root {
    --paper: #ffffff;
    --sky-yellow: #f6ef4c;
    --meadow: #8fe02a;
    --grass: #49c61c;
    --back-panel: #b2f318;
    --title-blue: #1420c8;
    --title-red: #e41c1c;
    --mark-blue: #1836c0;
    --ink: #1a1a1a;
    --dash: #ffffff;
  }
  html, body {
    margin: 0;
    padding: 0;
    overflow: hidden;
    background: var(--paper);
  }
  .cover-canvas {
    position: relative;
    width: 1200px;
    height: 1000px;
    overflow: hidden;
    background: var(--paper);
  }
  .wrap {
    position: absolute;
    left: 0;
    top: 68px;
    width: 1200px;
    height: 880px;
    background: linear-gradient(to bottom,
      var(--sky-yellow) 0%,
      var(--sky-yellow) 34%,
      #c9ea3a 42%,
      var(--meadow) 52%,
      var(--grass) 100%);
  }
  .back-panel {
    position: absolute;
    left: 0;
    top: 0;
  }
  .spine-title {
    position: absolute;
    left: 604px;
    top: 438px;
    transform: translate(-50%, -50%) rotate(-90deg);
    font-family: "Arimo", Arial, sans-serif;
    font-size: 30px;
    line-height: 1;
    color: var(--title-red);
    white-space: nowrap;
    margin: 0;
  }
  .spine-mark {
    position: absolute;
    left: 586px;
    top: 652px;
    display: flex;
    flex-direction: column;
    align-items: center;
    gap: 4px;
    width: 36px;
  }
  .mark-dot {
    border-radius: 50%;
    background: var(--mark-blue);
  }
  .spine-mark .mark-dot { width: 26px; height: 26px; }
  .mark-name {
    font-family: "Arimo", Arial, sans-serif;
    font-size: 10px;
    color: var(--mark-blue);
  }
  .front-mark {
    position: absolute;
    left: 1104px;
    top: 34px;
    display: flex;
    flex-direction: column;
    align-items: center;
    gap: 5px;
    width: 80px;
  }
  .front-mark .mark-dot { width: 52px; height: 52px; }
  .brain-art {
    position: absolute;
    left: 780px;
    top: 80px;
    width: 240px;
    height: 220px;
    border-radius: 48% 52% 45% 55%;
    background: radial-gradient(circle at 35% 35%, #f4a13c 0%, #b9d65a 55%, rgba(150,200,120,0) 78%);
    opacity: 0.85;
  }
  .title-block {
    position: absolute;
    left: 640px;
    top: 18px;
    width: 520px;
    text-align: center;
    font-family: "Tinos", "Times New Roman", serif;
    margin: 0;
  }
  .title-series {
    display: block;
    font-weight: 700;
    font-size: 104px;
    line-height: 100px;
    color: var(--title-blue);
    letter-spacing: 1px;
  }
  .title-main {
    display: block;
    font-weight: 400;
    font-size: 84px;
    line-height: 86px;
    color: var(--title-red);
    margin-top: 2px;
  }
  .author {
    position: absolute;
    left: 945px;
    top: 314px;
    display: flex;
    align-items: center;
    gap: 9px;
    font-family: "Arimo", Arial, sans-serif;
    font-size: 16px;
    color: var(--ink);
    margin: 0;
  }
  .author::before {
    content: "";
    width: 17px;
    height: 17px;
    border-radius: 50%;
    background: var(--title-red);
  }
  .swing-ring {
    position: absolute;
    left: 0;
    top: 0;
  }
  .golfer-photo {
    position: absolute;
    left: 632px;
    top: 410px;
    width: 500px;
    height: 470px;
    border-radius: 38% 30% 0 0;
    background: linear-gradient(160deg, #2a3340 0%, #e8b796 22%, #3b9ee0 48%, #2f86cc 75%, #c9c9c0 100%);
    opacity: 0.9;
  }
</style>
</head>
<body>
<main class="cover-canvas">
  <section class="wrap">
    <svg class="back-panel" width="1200" height="880" viewBox="0 0 1200 880" aria-hidden="true">
      <rect x="68" y="58" width="475" height="750" fill="var(--back-panel)"/>
      <rect x="68" y="58" width="475" height="750" fill="none"
            stroke="var(--back-panel)" stroke-width="20" stroke-dasharray="38 32"/>
    </svg>

    <p class="spine-title">GOLF Silent Tee Stance</p>
    <div class="spine-mark">
      <span class="mark-dot"></span>
      <span class="mark-name">Mindpath</span>
    </div>

    <div class="brain-art" role="img" aria-label="Illustration of a colourful brain behind the title"></div>

    <h1 class="title-block">
      <span class="title-series">GOLF</span>
      <span class="title-main">Silent Tee<br>Stance</span>
    </h1>

    <div class="front-mark">
      <span class="mark-dot"></span>
      <span class="mark-name">Mindpath</span>
    </div>

    <p class="author">Dana Merrow.H.Ed</p>

    <svg class="swing-ring" width="1200" height="880" viewBox="0 0 1200 880" aria-hidden="true">
      <path d="M885 385 A250 250 0 0 1 1085 740" fill="none" stroke="var(--dash)"
            stroke-width="8" stroke-dasharray="12 10" opacity="0.9"/>
      <path d="M710 700 A240 240 0 0 0 800 840" fill="none" stroke="var(--dash)"
            stroke-width="8" stroke-dasharray="12 10" opacity="0.9"/>
    </svg>

    <div class="golfer-photo" role="img" aria-label="Photograph of a golfer in a blue shirt and cap finishing a driver swing"></div>
  </section>
</main>
</body>
</html>
```